Design template for Opencart fast food takeaway website

We are looking for templates for fast food takeaway websites powered by the OpenCart framework.

The task involves 2 stages, firstly creating a mock-up which you will submit as an image. If we like your design, you'll then be required to implement it as an OpenCart template. We may not limit this competition to just one winner, ideally we would like a number of designs that we can then offer to our clients. We will pay $125 per template delivered ready to install (fully coded).

Our clients are either Chinese or Indian fast food takeaway businesses in the UK, all of whom offer delivery. We have created a dummy website based using the default template and you will see a link at the bottom left for a mobile version. However we would like our new templates to be responsive through using Bootstrap.

Please use the food images in the zip.

Dummy website: http://www.chinese.dishportalworks.co.uk/
OpenCart Version.1.5.6.4

```html
<!DOCTYPE html>
<html lang="en">
<head>
<meta charset="utf-8">
<title>Hanami Chinese Takeaway</title>
<link href="https://fonts.googleapis.com/css2?family=PT+Serif:wght@400;700&family=Open+Sans:wght@400;600&display=swap" rel="stylesheet">
<style>
:root{
  --orange:#f7861c;
  --orange-dark:#e06d0a;
  --logo:#c9501c;
  --text:#333;
  --muted:#888;
  --line:#e2e2e2;
  --dark:#3f3f3f;
  --teal:#2b9a9a;
  --page:#efefef;
  --tint:#e8f3f3;
}
*{box-sizing:border-box;margin:0;padding:0}
html,body{width:787px;height:1200px;overflow:hidden;background:var(--page)}
body{font-family:"Open Sans",sans-serif;color:var(--text);position:relative}
.sheet{position:absolute;left:41px;top:0;width:705px;height:1165px;background:#fff}
.abs{position:absolute}

/* header */
.welcome-line{left:567px;top:4px;font-size:6.5px;color:#555}
.welcome-line a{color:var(--orange);text-decoration:none}
.currency{left:346px;top:24px;font-size:7px;color:#555;letter-spacing:4px}
.top-links{left:528px;top:25px;font-size:6.5px;color:#666}
.top-links span{padding:0 4px;border-right:1px solid #ccc}
.top-links span:last-child{border:none}
.logo{left:66px;top:16px;color:var(--logo);font-family:"PT Serif",serif;font-weight:700;line-height:1}
.logo .name{font-size:32px;letter-spacing:1px}
.logo .sub{font-size:10px;letter-spacing:3.2px;margin-top:3px}
.cart{left:589px;top:45px;font-size:7.5px;color:#555;display:flex;align-items:center;gap:5px}
.cart .ic{width:18px;height:18px;border-radius:50%;background:#444;display:flex;align-items:center;justify-content:center}
.cart b{color:#1d6fb8;font-weight:600}

.nav{left:52px;top:75px;width:683px;height:28px;background:var(--orange);display:flex;align-items:center;font-family:"PT Serif",serif;font-size:8.5px;color:#fff}
.nav .home{width:30px;height:100%;display:flex;align-items:center;justify-content:center;border-right:1px solid #f9a95e}
.nav .item{padding:0 8px;border-right:1px solid #f9a95e;line-height:11px}
.nav .search{margin-left:auto;margin-right:6px;width:151px;height:16px;background:#fff;font-size:6.5px;color:#aaa;padding:4px 5px;position:relative}
.nav .search svg{position:absolute;right:5px;top:4px}

/* hero */
.hero{left:52px;top:115px;width:683px;height:314px;background:radial-gradient(ellipse at 40% 45%,#d86a2a 0%,#6f8a2a 35%,#3d4a1e 60%,#161616 100%)}
.promo{left:560px;top:179px;width:149px;height:229px;background:var(--orange);color:#fff;text-align:center;padding:17px 10px}
.promo h2{font-family:"PT Serif",serif;font-weight:400;font-size:23px;letter-spacing:.5px}
.promo p{font-size:6.3px;line-height:10.5px;margin-top:8px}
.promo .btn{display:inline-block;margin-top:13px;background:#fff;color:var(--orange);font-family:"PT Serif",serif;font-size:7px;border:2px solid #e85570;border-radius:2px;padding:5px 12px}

.thumbs{left:52px;top:435px;width:683px;height:61px;background:#4a4a4a;display:flex;gap:6px;padding:6px 4px}
.thumb{flex:1;height:48px}
.thumb:nth-child(1){background:linear-gradient(135deg,#3b6b22,#d2612a,#f0efe8)}
.thumb:nth-child(2){background:linear-gradient(135deg,#5e8a2a,#c7783a,#d8d0c4)}
.thumb:nth-child(3){background:linear-gradient(135deg,#efe8dd,#d99a55,#f3eee6)}
.thumb:nth-child(4){background:linear-gradient(135deg,#f4f0ea,#d8a75e,#c73a3a)}
.thumb:nth-child(5){background:linear-gradient(135deg,#4a8a2a,#f1d04a,#f5f2ea)}
.thumb:nth-child(6){background:linear-gradient(135deg,#c73c2a,#5e8f2a,#e9e3da)}
.arrow{top:456px;width:16px;height:18px;background:#444;display:flex;align-items:center;justify-content:center}

/* welcome */
.welcome-img{left:87px;top:520px;width:166px;height:118px;border-radius:50%;background:radial-gradient(ellipse,#7a3a1a 0%,#a65a2a 35%,#f4f4f0 62%,#fff 75%)}
.welcome-title{left:280px;top:528px;font-family:"PT Serif",serif;color:var(--orange);font-size:25px;font-weight:400}
.welcome-text{left:280px;top:563px;width:433px;font-size:6.6px;line-height:11.6px;color:#666}
.order-btn{left:620px;top:624px;width:73px;height:22px;background:var(--orange);color:#fff;font-family:"PT Serif",serif;font-size:9px;text-align:center;line-height:22px;border-radius:2px}

/* featured */
.feat-bar{left:52px;top:684px;width:683px;height:18px;background:var(--tint)}
.feat-tab{left:52px;top:684px;width:61px;height:18px;background:var(--orange);color:#fff;font-family:"PT Serif",serif;font-weight:700;font-size:8px;line-height:18px;padding-left:9px}
.products{left:52px;top:702px;width:683px;height:238px;border:1px solid var(--line);display:flex}
.product{flex:1;border-right:1px solid var(--line);padding:15px 5px 0;position:relative}
.product:last-child{border:none}
.product .img{height:110px}
.product:nth-child(1) .img{background:linear-gradient(135deg,#e9eef4,#e46a2a,#d04a1a,#2f5fa0)}
.product:nth-child(2) .img{background:linear-gradient(135deg,#6a9a2a,#c08a4a,#4a7a1a,#eae4d6)}
.product:nth-child(3) .img{background:linear-gradient(135deg,#f6f4f2,#b83030,#8a2020,#f2f0ee)}
.product:nth-child(4) .img{background:linear-gradient(135deg,#f4f2ea,#d8a028,#e0b040,#f6f4ee)}
.product h3{font-family:"PT Serif",serif;font-weight:400;font-size:9.2px;margin-top:19px;color:#333}
.product p{font-size:6.3px;line-height:11.5px;color:#777;margin-top:6px}
.stars{font-size:9px;letter-spacing:1px;margin-top:11px;color:#bbb}
.stars b{color:var(--teal);font-weight:400}
.buy{display:flex;align-items:center;margin-top:4px}
.price{width:78px;text-align:center;font-family:"PT Serif",serif;color:#1d7ac0;font-size:10px;font-weight:700}
.add{margin-left:auto;width:77px;height:17px;background:var(--orange);color:#fff;font-family:"PT Serif",serif;font-size:7.5px;text-align:center;line-height:17px}

/* newsletter */
.news-box{left:52px;top:953px;width:683px;height:61px;background:#f4f4f4;border:1px solid #ececec}
.news-title{left:61px;top:966px;font-family:"PT Serif",serif;font-size:11.5px;color:#333}
.news-input{left:61px;top:985px;width:264px;height:17px;border:1px solid #ddd;background:#fff;font-size:6.5px;color:#555;padding:4px 3px}
.news-go{left:325px;top:985px;width:28px;height:17px;background:var(--orange)}
.service-title{left:490px;top:968px;font-family:"PT Serif",serif;font-size:12px;color:#333}
.service-text{left:438px;top:989px;width:254px;text-align:center;font-size:6.4px;color:#777}

/* footer */
.foot-bar{left:41px;top:1029px;width:705px;height:31px;background:var(--dark);display:flex;align-items:center;font-family:"PT Serif",serif;font-size:7.5px;color:#eee;padding-left:11px}
.foot-bar .lk{padding:0 12px;border-right:1px solid #777;line-height:10px}
.foot-bar .lk:first-child{padding-left:0}
.foot-bar .lk:nth-child(6){border:none}
.follow{margin-left:auto;margin-right:27px;display:flex;align-items:center;gap:4px}
.follow i{width:13px;height:13px;border:1.3px solid #fff;border-radius:50%;display:block}
.follow span{margin-right:5px}
.col{top:1069px}
.col h4{font-family:"PT Serif",serif;font-weight:400;font-size:9px;color:#333;margin-bottom:5px}
.col li{list-style:none;font-size:6.5px;color:#666;line-height:14.5px}
.col li::before{content:"• ";color:#999}
.contact-row{display:flex;align-items:center;gap:9px;font-size:6.5px;color:#555;line-height:10px;margin-bottom:5px}
.contact-row .dot{width:17px;height:17px;border-radius:50%;background:var(--orange);flex:none;display:flex;align-items:center;justify-content:center}
.pay{left:604px;top:1177px;display:flex;gap:7px;align-items:center;font-weight:600;font-size:8px;color:#1d4f91}
.pay .sq{width:9px;height:9px;background:#1d4f91}
</style>
</head>
<body>
<div class="sheet"></div>

<header>
  <div class="abs welcome-line">Welcome visitor you can <a>login</a> or <a>create an account</a> .</div>
  <div class="abs logo"><div class="name">HANAMI</div><div class="sub">CHINESE TAKEAWAY</div></div>
  <div class="abs currency">€ £ $</div>
  <div class="abs top-links"><span>Home</span><span>Wish List (0)</span><span>My Account</span><span>Shopping Cart</span><span>Checkout</span></div>
  <div class="abs cart"><div class="ic"><svg width="9" height="9" viewBox="0 0 10 10"><path d="M0 1h2l1.5 5h5l1-4H3" fill="none" stroke="#fff" stroke-width="1"/><circle cx="4" cy="8.5" r=".9" fill="#fff"/><circle cx="8" cy="8.5" r=".9" fill="#fff"/></svg></div><b>Shopping Cart</b> 0 item(s) - $0.00 ▾</div>

  <nav class="abs nav">
    <div class="home"><svg width="12" height="11" viewBox="0 0 12 11"><path d="M6 0L0 5.5h1.7V11h3V7.5h2.6V11h3V5.5H12z" fill="#fff"/></svg></div>
    <div class="item">Starters</div>
    <div class="item">Main Dishes ⇂</div>
    <div class="item">Soups ⇂</div>
    <div class="item">Extra Dishes</div>
    <div class="item">Drinks</div>
    <div class="search">Search<svg width="8" height="8" viewBox="0 0 8 8"><circle cx="3.2" cy="3.2" r="2.3" fill="none" stroke="#f7861c" stroke-width="1.3"/><path d="M5 5l2.5 2.5" stroke="#f7861c" stroke-width="1.4"/></svg></div>
  </nav>
</header>

<main>
  <div class="abs hero" role="img" aria-label="Photo of stir-fried vegetables with broccoli, peppers and cauliflower on white rice"></div>
  <div class="abs promo">
    <h2>MAURIS</h2>
    <p>Nulla a odio vel urna eleifend scrisque Sed quam lorem ullamcorper vitae conse quat convallis quis odio Curabitur varius urna sed orci imperdiet eget accumsan leo dignissim elementum, ante erat sagittis rhoncus diam eget arcu tempor faucibus fringilla quam vulputate.</p>
    <span class="btn">SHOP NOW</span>
  </div>

  <div class="abs thumbs">
    <div class="thumb" role="img" aria-label="Vegetable rice dish thumbnail"></div>
    <div class="thumb" role="img" aria-label="Chicken with green peppers thumbnail"></div>
    <div class="thumb" role="img" aria-label="Prawn toast thumbnail"></div>
    <div class="thumb" role="img" aria-label="Spring rolls thumbnail"></div>
    <div class="thumb" role="img" aria-label="Lemon chicken thumbnail"></div>
    <div class="thumb" role="img" aria-label="Stir-fry thumbnail"></div>
  </div>
  <div class="abs arrow" style="left:43px;border-radius:9px 0 0 9px"><svg width="6" height="8" viewBox="0 0 6 8"><path d="M5 0L1 4l4 4" fill="none" stroke="#fff" stroke-width="1.5"/></svg></div>
  <div class="abs arrow" style="left:729px;border-radius:0 9px 9px 0"><svg width="6" height="8" viewBox="0 0 6 8"><path d="M1 0l4 4-4 4" fill="none" stroke="#fff" stroke-width="1.5"/></svg></div>

  <section>
    <div class="abs welcome-img" role="img" aria-label="Plate of crispy shredded beef with cucumber garnish"></div>
    <h1 class="abs welcome-title">Welcome</h1>
    <p class="abs welcome-text">Lorem ipsum dolor sit amet, consectetur adipiscing elit. Suspendisse eu ligula velit. Proin molestie, nisi at mollis adipiscing, lorem justo facilisis est, quis lobortis metus ante id turpis. Aliquam volutpat tortor nec sem interdum cursus. Donec eu lectus vel augue consequat ultricies at ut tellus. Aliquam erat volutpat Nunc nec enim sit amet magna volutpat eleifend. Morbi orci lacus, viverra non viverra sed, sagittis eget vitae sem adipiscing vestibulum. Etiam mattis luctus dapibus</p>
    <div class="abs order-btn">Order now</div>
  </section>

  <section>
    <div class="abs feat-bar"></div>
    <div class="abs feat-tab">Featured</div>
    <div class="abs products">
      <div class="product">
        <div class="img" role="img" aria-label="Sweet and sour chicken with peppers"></div>
        <h3>Cras porta massa at</h3>
        <p>Curabitur tempus velit in leo fermentum quis tincidunt lorem...</p>
        <div class="stars"><b>★★★★★</b></div>
        <div class="buy"><span class="price">$119.50</span><span class="add">Add to Cart</span></div>
      </div>
      <div class="product">
        <div class="img" role="img" aria-label="Chicken stir-fry with green peppers"></div>
        <h3>Fermentum quis tinci</h3>
        <p>Curabitur tempus velit in leo fermentum quis tincidunt lorem...</p>
        <div class="stars"><b>★</b>★★★★</div>
        <div class="buy"><span class="price">$1,177.00</span><span class="add">Add to Cart</span></div>
      </div>
      <div class="product">
        <div class="img" role="img" aria-label="Char siu pork strips with dipping sauce"></div>
        <h3>Fringilla eleifend</h3>
        <p>Curabitur tempus velit in leo fermentum quis tincidunt lorem...</p>
        <div class="stars"><b>★</b>★★★★</div>
        <div class="buy"><span class="price">$119.50</span><span class="add">Add to Cart</span></div>
      </div>
      <div class="product">
        <div class="img" role="img" aria-label="Chicken curry in a white bowl"></div>
        <h3>Metus placerat</h3>
        <p>Curabitur tempus velit in leo fermentum quis tincidunt lorem...</p>
        <div class="stars"><b>★★★</b>★★</div>
        <div class="buy"><span class="price">$119.50</span><span class="add">Add to Cart</span></div>
      </div>
    </div>
  </section>

  <section>
    <div class="abs news-box"></div>
    <div class="abs news-title">NEWSLETTER</div>
    <div class="abs news-input">Your email address</div>
    <div class="abs news-go"></div>
    <div class="abs service-title">24/7 CUSTOMER SERVICE</div>
    <div class="abs service-text">Nulla rhoncus blandit lacus in scelerisque leo donec urna lobor tis molestie.</div>
  </section>
</main>

<footer>
  <div class="abs foot-bar">
    <span class="lk">Fusce hen</span><span class="lk">Proin imper</span><span class="lk">Sed non sem</span><span class="lk">Nunc vel</span><span class="lk">Curabitur</span><span class="lk">Fermentum</span>
    <div class="follow"><span>Follow us on</span><i></i><i></i><i></i><i></i></div>
  </div>

  <div class="abs col" style="left:52px"><h4>Information</h4><ul><li>About Us</li><li>Delivery Information</li><li>Privacy Policy</li><li>Terms &amp; Conditions</li></ul></div>
  <div class="abs col" style="left:227px"><h4>Customer Service</h4><ul><li>Contact Us</li><li>Returns</li><li>Site Map</li><li>Brands</li><li>Gift Vouchers</li></ul></div>
  <div class="abs col" style="left:402px"><h4>My Account</h4><ul><li>My Account</li><li>Order History</li><li>Wish List</li><li>Newsletter</li><li>Specials</li></ul></div>
  <div class="abs col" style="left:577px"><h4>Contact Us</h4>
    <div class="contact-row"><span class="dot"><svg width="7" height="9" viewBox="0 0 7 9"><path d="M3.5 0A3.2 3.2 0 0 0 .3 3.2C.3 5.5 3.5 9 3.5 9s3.2-3.5 3.2-5.8A3.2 3.2 0 0 0 3.5 0z" fill="#fff"/><circle cx="3.5" cy="3.2" r="1.1" fill="#f7861c"/></svg></span><span>Wedddd have 152 guests and 14<br>members online</span></div>
    <div class="contact-row"><span class="dot"><svg width="8" height="8" viewBox="0 0 8 8"><path d="M1.5 0l1.5 2-1 1c.5 1.3 1.4 2.2 2.6 2.7l1-1 2 1.5-1 1.6C3.5 8 0 4.5.2 1.2z" fill="#fff"/></svg></span><span>Phone: +01 555 (010) 4827</span></div>
    <div class="contact-row"><span class="dot"><svg width="9" height="8" viewBox="0 0 9 8"><rect x="2" y="0" width="5" height="3" fill="#fff"/><rect x="0" y="3" width="9" height="4" rx="1" fill="#fff"/><rect x="2" y="5" width="5" height="3" fill="#fff" stroke="#f7861c" stroke-width=".6"/></svg></span><span>Fax: +01 555 (010) 4828</span></div>
  </div>

  <div class="abs pay"><span>VANTAPAY</span><span class="sq"></span><span>MERIDIAN</span><span>PayWell</span></div>
</footer>
</body>
</html>
```